Buch-/E-Book-Cover
Tolle Designerin. Tolles Ergebnis. Das beste war die reibungslose Kommunikation.
Zielgruppe
Wir verkaufen Trainings und vermitteln über unser Buch ein erstes vertieftes Wissen zum Thema Vermögensaufbau.
Aufgabenstellung
Es soll schlicht und schön sein, Angelehnt an Kluge Kinder arme Eltern, bzw. an Plane klug und werde frei von Bertram Quist.
Wir benötigen die AI, etc Dateien und die fertigen Dateien für Lesewelt.de Lumo sowie Lesewelt.de Books (ehemals Printfeld) mit fertigem Cover.
Vorgaben von Lesewelt.de über die Homepage. Anbei ein Beispiel (wegen Lesewelt.de Buchnummer etc) Abstände, Buchrücken etc.
Buch ca. 150 Seiten
https://www.lesewelt-beispiel.de/Gaertner-bleiben-ehrlich-Sommer-ruhigen/dp/7302958816 Front und Backcover kann man sich da ansehen.
Der Buchtitel ist 'Baue Mauern und bleibe frei' - - Lassen Sie uns freundschaftlich in entspannter Atmosphäre über Immobilien sprechen (der nebentitel so klein wie bei Kluge Kinder - Arme Eltern)
Rücktitel: Bitte zuerst Platzhalter.
Ich bitte um 5x8 inch, also wie DIN A 5, wir nehmen cremefarbenes Papier denke ich. Die Seitenzahl kann ich auf die Seite noch nicht sagen, wir haben aber 75 Din A4 Seiten, sprich nach Formatierung eher 160-165 Din A5. WErde ich Ihnen final nach dem Gewinn sagen.
Versuchen Sie mich mal aus dem einen Bild raus zu schneiden, und dass dann mit einem Layer über das cover zu legen.
2-3 Versionen wäre gut, mit 2-3 Bildern. Buchrücken ein kleines Bild von mir.
Seite vom Buch: Titel nochmal.

```html
<!DOCTYPE html>
<html lang="de">
<head>
<meta charset="utf-8">
<title>Baue Mauern und bleibe frei – Coverentwürfe</title>
<link href="https://fonts.googleapis.com/css2?family=Lato:wght@300;400;900&display=swap" rel="stylesheet">
<style>
  :root {
    --page: #ffffff;
    --cover-black: #0d0b0a;
    --gold: #c9b48a;
    --gold-soft: rgba(201, 180, 138, 0.55);
    --gold-fade: rgba(201, 180, 138, 0);
    --white: #ffffff;
    --suit: #4b3a32;
    --suit-dark: #3a2d27;
  }
  html, body {
    margin: 0;
    width: 1200px;
    height: 5000px;
    overflow: hidden;
    background: var(--page);
    font-family: "Lato", sans-serif;
  }
  .cover {
    position: absolute;
    left: 274px;
    width: 720px;
    height: 1160px;
    background: var(--cover-black);
    overflow: hidden;
  }
  .cover--one { top: 340px; }
  .cover--two { top: 1866px; height: 1158px; }
  .cover--three { top: 3390px; width: 730px; height: 1170px; }

  /* gold line ornament area */
  .line-pattern { position: absolute; }
  .cover--one .line-pattern {
    left: 0; top: 80px; width: 340px; height: 1080px;
    background: linear-gradient(90deg, var(--gold-soft), var(--gold-fade));
    clip-path: polygon(0 8%, 100% 30%, 100% 60%, 0 100%);
  }
  .cover--two .line-pattern {
    left: 0; top: 300px; width: 720px; height: 200px;
    background: linear-gradient(90deg, var(--gold-soft), var(--gold-fade) 45%, var(--gold-fade) 55%, var(--gold-soft));
    clip-path: polygon(0 0, 100% 30%, 100% 100%, 0 70%);
  }
  .cover--three .line-pattern {
    left: 0; top: 450px; width: 730px; height: 720px;
    background: linear-gradient(180deg, var(--gold-soft), var(--gold-fade) 80%);
    clip-path: polygon(0 0, 100% 12%, 100% 75%, 0 100%);
  }

  /* author photo area */
  .portrait {
    position: absolute;
    background: linear-gradient(180deg, var(--suit) 0%, var(--suit-dark) 100%);
    border-radius: 200px 200px 0 0;
  }
  .cover--one .portrait { left: 296px; top: 20px; width: 424px; height: 1140px; }
  .cover--two .portrait { left: 136px; top: 14px; width: 540px; height: 1144px; }
  .cover--three .portrait { left: 256px; top: 20px; width: 410px; height: 1150px; }

  .author-line {
    position: absolute;
    margin: 0;
    color: var(--white);
    font-size: 22px;
    line-height: 28px;
    font-weight: 400;
  }
  .cover--one .author-line { left: 60px; top: 48px; }
  .cover--two .author-line { left: 66px; top: 42px; }
  .cover--three .author-line { left: 64px; top: 46px; }

  .title {
    position: absolute;
    margin: 0;
    font-size: 104px;
    line-height: 92px;
    font-weight: 900;
    text-transform: uppercase;
  }
  .title span { display: block; }
  .title .is-white { color: var(--white); }
  .title .is-gold { color: var(--gold); }
  .title .is-light { font-weight: 300; color: var(--white); }
  .cover--one .title { left: 58px; top: 592px; }
  .cover--two .title { left: 64px; top: 556px; }
  .cover--three .title { left: 64px; top: 580px; line-height: 100px; }

  .subtitle {
    position: absolute;
    margin: 0;
    color: var(--white);
    font-size: 22px;
    line-height: 28px;
    font-weight: 400;
  }
  .cover--one .subtitle { left: 60px; top: 976px; }
  .cover--two .subtitle { left: 66px; top: 940px; }
  .cover--three .subtitle { left: 68px; top: 1010px; font-size: 26px; line-height: 32px; }
</style>
</head>
<body>

<section class="cover cover--one">
  <div class="line-pattern" role="img" aria-label="Goldenes geschwungenes Linienmuster"></div>
  <div class="portrait" role="img" aria-label="Porträtfoto des Autors im braunen Sakko, Arme verschränkt"></div>
  <p class="author-line">TILL VARNHAGEN –<br>Der WohnwertBerater</p>
  <h1 class="title">
    <span class="is-white">Baue</span>
    <span class="is-white">Mauern</span>
    <span class="is-gold">Und bleibe</span>
    <span class="is-gold">Frei</span>
  </h1>
  <p class="subtitle">Lassen Sie uns unter Freunden<br>in entspannter Atmosphäre<br>über Immobilien sprechen</p>
</section>

<section class="cover cover--two">
  <div class="line-pattern" role="img" aria-label="Goldenes Linienband quer über den Hintergrund"></div>
  <div class="portrait" role="img" aria-label="Foto des Autors stehend im braunen Anzug, Hände in den Taschen"></div>
  <p class="author-line">TILL VARNHAGEN –<br>Der WohnwertBerater</p>
  <h1 class="title">
    <span class="is-white">Baue</span>
    <span class="is-white">Mauern</span>
    <span class="is-gold">Und bleibe</span>
    <span class="is-gold">Frei</span>
  </h1>
  <p class="subtitle">Lassen Sie uns unter Freunden<br>in entspannter Atmosphäre<br>über Immobilien sprechen</p>
</section>

<section class="cover cover--three">
  <div class="line-pattern" role="img" aria-label="Goldene geschwungene Linien im unteren Bereich"></div>
  <div class="portrait" role="img" aria-label="Ganzkörperfoto des Autors im braunen Anzug"></div>
  <p class="author-line">TILL VARNHAGEN –<br>Der WohnwertBerater</p>
  <h1 class="title">
    <span class="is-gold">Baue</span>
    <span class="is-gold">Mauern</span>
    <span class="is-light">Und bleibe</span>
    <span class="is-light">Frei</span>
  </h1>
  <p class="subtitle">Lassen Sie uns unter Freunden in entspannter<br>Atmosphäre über Immobilien sprechen</p>
</section>

</body>
</html>
```